Zolqa..Hydrating sports energy drink

"Zolqa" is a hydrating, all-natural energy beverage geared towards health focused consumers and athletes
While other energy drinks are carbonated and artificially flavored, Zolqa's
light and refreshing all-natural formula tastes more like a sports drink without the heavy after effects
Zolqa's tropical, vitamin rich taste provides the hydration and burst of energy to help you perform at your best with out the calories....

Target Market(s)

hispanic males teen to 24 yrs old -with a cross over to the 18-35 yr old female due to it all-natural formula low in calories no sugar
this is a logo and bottle package design request. We have left it open to the arist vision
on how will look.

Thank you..Good luck!!!

Industry/Entity Type

Health

Requirements
Nice to have
• contrasting image ,

Several ideas have been submitted which look pretty good .

I like to have a contrasting design done as follows :

Think of a Spartan warrior caricature holding a shield in one hand , on the shield is our brand name Zolaqa
.. in the other hand he is holding a lighting bolt he is standing on a bluff over looking a clear refreshing looking lake

```html
<!DOCTYPE html>
<html lang="en">
<head>
<meta charset="utf-8">
<title>Zolqa Energy – Label</title>
<link href="https://fonts.googleapis.com/css2?family=Roboto:wght@400;700;900&display=swap" rel="stylesheet">
<style>
  :root {
    --ink: #000000;
    --white: #ffffff;
    --rail-dark: #5e5e5e;
    --rail-light: #e2e2e2;
    --green-deep: #0b3a10;
    --green: #1fa01f;
    --green-bright: #3fd12a;
    --blue-deep: #0a1e8c;
    --blue: #1a5fd6;
    --blue-bright: #2aa8f0;
    --red: #ff3a0a;
    --orange: #ff8a0c;
    --yellow: #ffd21a;
    --energy-blue: #1e8fe0;
    --wordmark: #e6e6e6;
  }
  html, body {
    margin: 0;
    padding: 0;
    width: 945px;
    height: 1200px;
    overflow: hidden;
    background: var(--ink);
  }
  .label {
    position: relative;
    width: 945px;
    height: 1200px;
    overflow: hidden;
    background: var(--ink);
    font-family: "Roboto", Arial, sans-serif;
  }
  .scene {
    position: absolute;
    left: 77px;
    top: 0;
    width: 792px;
    height: 880px;
  }
  .side-rail {
    position: absolute;
    top: 0;
    height: 1200px;
    display: flex;
    align-items: center;
  }
  .side-rail.left {
    left: 0;
    width: 77px;
    background: linear-gradient(90deg, var(--rail-dark), var(--rail-light) 55%, #9a9a9a);
  }
  .side-rail.right {
    left: 869px;
    width: 76px;
    background: linear-gradient(90deg, #9a9a9a, var(--rail-light) 45%, var(--rail-dark));
  }
  .rail-text {
    position: absolute;
    writing-mode: vertical-rl;
    white-space: nowrap;
    font-weight: 700;
    font-size: 51px;
    line-height: 77px;
    letter-spacing: 1px;
    color: var(--ink);
    text-align: center;
  }
  .rail-text.left {
    left: 0;
    width: 77px;
    top: 862px;
    height: 300px;
    transform: rotate(180deg);
  }
  .rail-text.right {
    left: 869px;
    width: 76px;
    top: 656px;
    height: 520px;
  }
  .headline {
    position: absolute;
    left: 77px;
    width: 792px;
    text-align: center;
    color: var(--white);
    font-weight: 700;
    text-shadow: 0 0 10px rgba(0,0,0,0.9), 0 0 3px rgba(0,0,0,0.9);
    margin: 0;
    line-height: 1;
  }
  .headline.boosts { top: 34px; font-size: 86px; }
  .headline.performance { top: 130px; font-size: 57px; }
  .brand-name {
    position: absolute;
    left: 77px;
    width: 792px;
    top: 832px;
    text-align: center;
    font-weight: 900;
    font-size: 218px;
    line-height: 1;
    letter-spacing: 2px;
    color: var(--wordmark);
    margin: 0;
  }
  .brand-tagline {
    position: absolute;
    left: 77px;
    width: 792px;
    top: 1052px;
    text-align: center;
    font-weight: 400;
    font-size: 66px;
    line-height: 1;
    color: var(--energy-blue);
    margin: 0;
  }
</style>
</head>
<body>
<div class="label">
  <svg class="scene" viewBox="0 0 792 880" role="img" aria-label="Illustration of athletes leaping, kicking and flipping in silhouette over green, blue and orange bands with swirling lines, and dark grass and plants along the bottom">
    <defs>
      <linearGradient id="band-green" x1="0" y1="0" x2="0" y2="1">
        <stop offset="0" stop-color="var(--green-deep)"/>
        <stop offset="0.5" stop-color="var(--green)"/>
        <stop offset="0.75" stop-color="var(--green-bright)"/>
        <stop offset="1" stop-color="#000"/>
      </linearGradient>
      <linearGradient id="band-blue" x1="0" y1="0" x2="0" y2="1">
        <stop offset="0" stop-color="var(--blue-deep)"/>
        <stop offset="0.55" stop-color="var(--blue)"/>
        <stop offset="0.75" stop-color="var(--blue-bright)"/>
        <stop offset="1" stop-color="#000"/>
      </linearGradient>
      <linearGradient id="band-orange" x1="0" y1="0" x2="0" y2="1">
        <stop offset="0" stop-color="var(--red)"/>
        <stop offset="0.45" stop-color="var(--orange)"/>
        <stop offset="0.72" stop-color="var(--yellow)"/>
        <stop offset="1" stop-color="#000"/>
      </linearGradient>
      <linearGradient id="band-white" x1="0" y1="0" x2="0" y2="1">
        <stop offset="0" stop-color="#ffffff"/>
        <stop offset="0.75" stop-color="#f0f0f0"/>
        <stop offset="1" stop-color="#000"/>
      </linearGradient>
      <linearGradient id="ground-fade" x1="0" y1="0" x2="0" y2="1">
        <stop offset="0" stop-color="#000" stop-opacity="0"/>
        <stop offset="0.6" stop-color="#000" stop-opacity="0.85"/>
        <stop offset="1" stop-color="#000" stop-opacity="1"/>
      </linearGradient>
    </defs>
    <rect x="0" y="0" width="214" height="880" fill="url(#band-green)"/>
    <rect x="214" y="0" width="56" height="880" fill="url(#band-white)"/>
    <rect x="270" y="0" width="250" height="880" fill="url(#band-blue)"/>
    <rect x="520" y="0" width="54" height="880" fill="url(#band-white)"/>
    <rect x="574" y="0" width="218" height="880" fill="url(#band-orange)"/>
    <rect x="0" y="640" width="792" height="240" fill="url(#ground-fade)"/>
  </svg>

  <div class="side-rail left"></div>
  <div class="side-rail right"></div>
  <span class="rail-text left">NO SUGAR</span>
  <span class="rail-text right">NO PRESERVATIVES</span>

  <h1 class="headline boosts">BOOSTS</h1>
  <p class="headline performance">YOUR PERFORMANCE</p>

  <h2 class="brand-name">ZOLQA</h2>
  <p class="brand-tagline">ENERGY</p>
</div>
</body>
</html>
```